High profile consultancy

We need a web design for a company called BK Services. BK as abbreviation for Bold Keystone.

Company focusses on Sourcing (BK Sourcing, focus on ICT), Metrics (BK Metrics; focus on business case analysis and trends in ICT) and Software (BK software; to be developed later on; mainly tools supporting BK soucing and metrics)

Customers base consists of large enterprises, >1000 employees.

Site needs to have menu's for
- services
- login
- about
and a special area ' inspire ' to be able to communicate topics that should inspire our customers to contact us.

but key; it schould communicate our expertise and focus on deep knowlegde of ICT sourcing

Reason: please advice on content management systems to be used to maintain site also please advice on Trovix search clickbids. Will provide feedback on designs shortly.

Target Market(s)

CIO's; board of directors;
company excels in ICT / business knowledge and ability to execute; creates / optimizes relations between ICT suppliers and enterprises.

Requirements
Must have
• website should be easily be found; adaptive by design; accessible by all browsers.
• Need to have a login section for later use
Nice to have
• usage of (draft) logo. see upload.

```html
<!DOCTYPE html>
<html lang="en">
<head>
<meta charset="utf-8">
<title>BK Services – Bold Keystone</title>
<link rel="stylesheet" href="https://fonts.googleapis.com/css2?family=Cormorant+Garamond:wght@500;600&family=Roboto+Condensed:wght@400&family=Open+Sans:ital,wght@0,400;0,600;0,700;1,400&display=swap">
<style>
:root{
  --brand:#0b4aa8;
  --brand-dark:#0a3a8c;
  --footer:#0c3f95;
  --footer-line:#2a5bb0;
  --ink:#2b2b2b;
  --muted:#8a8a8a;
  --rule:#d8d8d8;
  --bottom:#2a2a2a;
  --white:#ffffff;
}
*{margin:0;padding:0;box-sizing:border-box}
html,body{width:708px;height:1200px;overflow:hidden;background:var(--white)}
body{position:relative;font-family:"Open Sans",Arial,sans-serif;color:var(--ink)}
.abs{position:absolute}
a{color:inherit;text-decoration:none}

/* header */
.site-header{left:0;top:0;width:708px;height:53px;background:var(--white);border-bottom:3px solid var(--brand)}
.account-tab{left:519px;top:0;width:94px;height:13px;background:var(--brand);color:var(--white);font-size:6.5px;font-weight:700;letter-spacing:.5px;display:flex;align-items:center;justify-content:center;gap:6px}
.brand{left:95px;top:14px;display:flex;align-items:center;gap:5px}
.brand-mark{width:20px;height:20px;border-radius:50%;background:var(--brand)}
.brand-name{font-family:"Cormorant Garamond",Georgia,serif;font-weight:600;font-size:17px;color:var(--brand-dark)}
.main-nav{left:350px;top:28px;display:flex;gap:0;font-family:"Cormorant Garamond",Georgia,serif;font-size:8px;letter-spacing:1px;color:#555}
.main-nav a{display:block}
.main-nav a+a{margin-left:38px}

/* hero */
.hero{left:0;top:56px;width:708px;height:349px;background:linear-gradient(180deg,#0a1f5c 0%,#1638a0 45%,#2a5fd8 72%,#0a2a80 88%,#1a4ec4 100%)}
.hero-title{left:327px;top:128px;font-family:"Cormorant Garamond",Georgia,serif;font-variant:small-caps;font-weight:500;font-size:19px;color:var(--white);letter-spacing:.6px}
.hero-text{left:327px;top:156px;width:300px;font-size:8px;font-weight:600;line-height:13px;color:var(--white)}

/* services */
.service{width:165px}
.section-title{font-family:"Roboto Condensed",Arial,sans-serif;font-size:11px;letter-spacing:.6px;color:#555}
.photo{background:linear-gradient(135deg,#d9dde3,#9aa3ad)}
.service .photo{margin-top:9px;width:165px;height:77px}
.body-copy{font-size:5.6px;line-height:9.5px;color:#333}
.service .body-copy{margin-top:10px}
.read-more{display:block;font-size:5.6px;font-weight:700;color:var(--brand);letter-spacing:.4px}
.service .read-more{margin-top:14px}

/* inspire */
.inspire-photo{left:95px;top:626px;width:117px;height:131px;background:linear-gradient(135deg,#e9ecef,#aeb6bf)}
.inspire{left:229px;top:626px;width:206px}
.inspire .body-copy{margin-top:8px}
.inspire .body-copy+.body-copy{margin-top:6px}
.inspire .read-more{margin-top:8px}

.news{left:448px;top:626px;width:137px}
.news .section-title{border-bottom:3px solid #e2e2e2;padding-bottom:1px}
.news-item{display:flex;gap:8px;margin-top:9px}
.news-item:first-of-type{margin-top:9px}
.news-thumb{width:31px;height:31px;background:linear-gradient(135deg,#e6e8ea,#9ea6ae);flex:none}
.news-text{font-size:5.4px;line-height:8.5px;color:#333}
.news-date{color:var(--muted);margin-top:3px}

.divider{left:95px;top:786px;width:518px;height:1px;background:var(--rule)}

/* testimonials */
.testimonial{top:810px;width:131px;text-align:center}
.avatar{width:38px;height:38px;border-radius:50%;margin:0 auto;background:linear-gradient(135deg,#c9b8a8,#6a5a50)}
.person{margin-top:8px;font-size:6.5px;font-weight:600;color:#222}
.company{margin-top:2px;font-size:5.5px;font-style:italic;color:var(--muted)}
.quote{margin-top:9px;text-align:left;font-size:5.5px;font-style:italic;line-height:8.5px;color:#444;padding:0 4px}
.quote-bar{margin-top:8px;height:3px;background:#e2e2e2}

/* footer */
.site-footer{left:0;top:949px;width:708px;height:222px;background:var(--footer);color:var(--white)}
.footer-split{left:361px;top:949px;width:1px;height:222px;background:#0a3580;box-shadow:1px 0 0 #1b54b4}
.f-col{color:var(--white)}
.f-head{font-size:7px;font-weight:700;display:flex;justify-content:space-between;align-items:center;padding-bottom:4px;border-bottom:1px solid var(--footer-line)}
.f-text{font-size:5.6px;line-height:8.5px;margin-top:8px;color:#dfe8f8}
.f-list{list-style:none;margin-top:6px;font-size:5.4px;font-weight:600}
.f-list li{height:10.5px;display:flex;align-items:center;gap:5px}
.f-list li::before{content:"";width:0;height:0;border-left:2.5px solid #cfdaf0;border-top:2px solid transparent;border-bottom:2px solid transparent}
.contact-line{display:flex;align-items:center;gap:9px;font-size:5.4px;font-weight:600;height:13px}
.field{background:var(--white);color:#777;font-size:5.4px;padding:4px 5px}
.send{background:linear-gradient(#6a6e74,#44484e);color:var(--white);font-size:5.6px;font-weight:700;display:flex;align-items:center;justify-content:center;border-radius:2px}
.social{display:flex;gap:7px}
.social span{width:15px;height:15px;border-radius:50%;background:var(--white)}

.bottom-bar{left:0;top:1171px;width:708px;height:29px;background:var(--bottom);color:#8d8d8d;font-size:5.6px}
.bottom-bar .copy{left:96px;top:12px}
.bottom-bar .legal{left:505px;top:12px;display:flex;gap:6px}
</style>
</head>
<body>

<header class="abs site-header">
  <div class="abs account-tab"><a href="#">LOGIN</a><span>|</span><a href="#">REGISTER</a></div>
  <div class="abs brand"><span class="brand-mark"></span><span class="brand-name">BK Services</span></div>
  <nav class="abs main-nav"><a href="#">HOME</a><a href="#">SERVICES</a><a href="#">ABOUT</a><a href="#">INSPIRE</a><a href="#">CONTACT</a></nav>
</header>

<section class="abs hero" role="img" aria-label="Night city skyline lit in blue along a waterfront"></section>
<h1 class="abs hero-title">Ensuring the Quality of Your Service</h1>
<p class="abs hero-text">Lorem ipsum dolor sit amet, consectetur adipisicing elit, sed do eiusmod tempor incididunt ut labore et dolore magna aliqua.</p>

<article class="abs service" style="left:95px;top:434px">
  <h2 class="section-title">BK SOURCING</h2>
  <div class="photo" role="img" aria-label="Business team meeting around a table"></div>
  <p class="body-copy">Lorem ipsum dolor sit amet, consectetur adipisicing elit, sed do eiusmod tempor incididunt ut labore et dolore magna aliqua. Ut enim ad minim veniam, quis nostrud exercitation.</p>
  <a class="read-more" href="#">READ MORE &rsaquo;</a>
</article>
<article class="abs service" style="left:272px;top:434px">
  <h2 class="section-title">BK METRICS</h2>
  <div class="photo" role="img" aria-label="Hands reviewing printed bar charts with a pen"></div>
  <p class="body-copy">Lorem ipsum dolor sit amet, consectetur adipisicing elit, sed do eiusmod tempor incididunt ut labore et dolore magna aliqua. Ut enim ad minim veniam, quis nostrud exercitation.</p>
  <a class="read-more" href="#">READ MORE &rsaquo;</a>
</article>
<article class="abs service" style="left:449px;top:434px">
  <h2 class="section-title">BK SOFTWARE</h2>
  <div class="photo" role="img" aria-label="Finger touching a tablet showing charts"></div>
  <p class="body-copy">Lorem ipsum dolor sit amet, consectetur adipisicing elit, sed do eiusmod tempor incididunt ut labore et dolore magna aliqua. Ut enim ad minim veniam, quis nostrud exercitation.</p>
  <a class="read-more" href="#">READ MORE &rsaquo;</a>
</article>

<div class="abs inspire-photo" role="img" aria-label="Two business people discussing documents in a bright office"></div>
<section class="abs inspire">
  <h2 class="section-title">INSPIRE</h2>
  <p class="body-copy">Lorem ipsum dolor sit amet, consectetur adipisicing elit, sed do eiusmod tempor incididunt ut labore et dolore magna aliqua. Ut enim ad minim veniam, quis nostrud exercitation. Lorem ipsum dolor sit amet, consectetur adipisicing elit, sed do eiusmod tempor incididunt ut labore et dolore magna aliqua. Ut enim ad minim veniam, quis nostrud exercitation.</p>
  <p class="body-copy">Lorem ipsum dolor sit amet, consectetur adipisicing elit, sed do eiusmod tempor incididunt ut labore et dolore magna aliqua. Ut enim ad minim veniam, quis nostrud exercitation.</p>
  <a class="read-more" href="#">READ MORE &rsaquo;</a>
</section>

<aside class="abs news">
  <h2 class="section-title">LATEST NEWS</h2>
  <div class="news-item"><div class="news-thumb" role="img" aria-label="Presenter at a whiteboard"></div><div class="news-text">Lorem ipsum dolor sit amet, consectetur adipisicing elit<div class="news-date">26 May, 2013</div></div></div>
  <div class="news-item"><div class="news-thumb" role="img" aria-label="Woman in an office"></div><div class="news-text">Lorem ipsum dolor sit amet, consectetur adipisicing elit<div class="news-date">26 May, 2013</div></div></div>
  <div class="news-item"><div class="news-thumb" role="img" aria-label="Business people talking"></div><div class="news-text">Lorem ipsum dolor sit amet, consectetur adipisicing elit<div class="news-date">26 May, 2013</div></div></div>
</aside>

<div class="abs divider"></div>

<figure class="abs testimonial" style="left:144px">
  <div class="avatar" role="img" aria-label="Client portrait"></div>
  <div class="person">Daniel Marsh</div><div class="company">Arden Agency</div>
  <blockquote class="quote">"Lorem ipsum dolor sit amet, consectetur adipisicing elit, sed do eiusmod tempor incididunt ut labore et dolore magna aliqua.</blockquote>
  <div class="quote-bar"></div>
</figure>
<figure class="abs testimonial" style="left:286px">
  <div class="avatar" role="img" aria-label="Client portrait"></div>
  <div class="person">Daniel Marsh</div><div class="company">Vell Corporation</div>
  <blockquote class="quote">"Lorem ipsum dolor sit amet, consectetur adipisicing elit, sed do eiusmod tempor incididunt ut labore et dolore magna aliqua.</blockquote>
  <div class="quote-bar"></div>
</figure>
<figure class="abs testimonial" style="left:428px">
  <div class="avatar" role="img" aria-label="Client portrait"></div>
  <div class="person">Daniel Marsh</div><div class="company">Outsourcing Azure</div>
  <blockquote class="quote">"Lorem ipsum dolor sit amet, consectetur adipisicing elit, sed do eiusmod tempor incididunt ut labore et dolore magna aliqua.</blockquote>
  <div class="quote-bar"></div>
</figure>

<footer class="abs site-footer"></footer>
<div class="abs footer-split"></div>

<div class="abs f-col" style="left:97px;top:982px;width:95px">
  <div class="f-head">About Us
    <svg width="7" height="7" viewBox="0 0 10 10"><circle cx="5" cy="3" r="2.4" fill="#6d8fd0"/><path d="M1 10a4 4 0 0 1 8 0z" fill="#6d8fd0"/></svg></div>
  <p class="f-text">Duis mollis, est non commodo luctus, nisi erat porttitor ligula, eget lacinia odio sem nec elit. Vestibulum id ligula porta felis euismod semper. Integer posuere erat a ante.</p>
  <p class="f-text" style="margin-top:7px">Vestibulum id ligula porta felis euismod semper. Integer posuere erat a ante.</p>
</div>

<div class="abs f-col" style="left:230px;top:982px;width:95px">
  <div class="f-head">Contact Details
    <svg width="8" height="6" viewBox="0 0 10 7"><rect x=".5" y=".5" width="9" height="6" fill="none" stroke="#6d8fd0"/><path d="M.5 .5l4.5 3.5 4.5-3.5" fill="none" stroke="#6d8fd0"/></svg></div>
  <p class="f-text">There are many variations of passages of Lorem Ipsum available, but the majority have suffered alteration.</p>
  <div style="margin-top:10px">
    <div class="contact-line"><svg width="6" height="8" viewBox="0 0 6 8"><path d="M3 0a3 3 0 0 1 3 3c0 2-3 5-3 5S0 5 0 3a3 3 0 0 1 3-3z" fill="#0a2a66"/></svg>Northbridge</div>
    <div class="contact-line"><svg width="7" height="5" viewBox="0 0 7 5"><rect width="7" height="5" fill="#0a2a66"/></svg>info@bkservices.example</div>
    <div class="contact-line"><svg width="7" height="7" viewBox="0 0 7 7"><path d="M1 0l2 2-1 1 2 2 1-1 2 2-1 1C3 7 0 4 0 1z" fill="#0a2a66"/></svg>555-01234-56789</div>
  </div>
</div>

<div class="abs f-col" style="left:96px;top:1095px;width:95px">
  <div class="f-head" style="border:0;padding:0">Navigation</div>
  <ul class="f-list"><li>Home</li><li>About</li><li>Services</li><li>Contact</li></ul>
</div>
<div class="abs f-col" style="left:228px;top:1095px;width:95px">
  <div class="f-head" style="border:0;padding:0">Services</div>
  <ul class="f-list"><li>Sourcing BK</li><li>Quality Assurance</li><li>Metrics BK</li><li>Software BK</li></ul>
</div>

<div class="abs f-col" style="left:393px;top:982px;width:221px">
  <div class="f-head" style="border:0;padding:0">We'd love to hear from you.
    <svg width="9" height="7" viewBox="0 0 10 8"><ellipse cx="5" cy="3.5" rx="4.5" ry="3" fill="none" stroke="#6d8fd0"/></svg></div>
  <p class="f-text" style="margin-top:6px">If you have questions or inquires, please don't hesitate to contact us through phone or you can send your message using the contact form below:</p>
</div>
<div class="abs field" style="left:393px;top:1023px;width:101px;height:14px">Name</div>
<div class="abs field" style="left:393px;top:1043px;width:101px;height:14px">Email</div>
<div class="abs field" style="left:393px;top:1063px;width:101px;height:14px">Phone</div>
<div class="abs field" style="left:504px;top:1023px;width:110px;height:55px">Message</div>
<div class="abs send" style="left:565px;top:1089px;width:48px;height:16px">Send Email</div>

<div class="abs f-col" style="left:393px;top:1118px">
  <div class="f-head" style="border:0;padding:0;font-size:6.5px">Social Links</div>
  <div class="social" style="margin-top:7px"><span></span><span></span><span></span><span></span></div>
</div>

<div class="abs bottom-bar">
  <div class="abs copy">Copyright 2013 © BK Services - All Rights Reserved</div>
  <div class="abs legal"><span>Site Map</span><span>•</span><span>Privacy Policy</span><span>•</span><span>Disclaimer</span></div>
</div>

</body>
</html>
```